Manufacturers Catalog Cover Page

We are looking to have a cover to our catalog page designed. I currently have begun work for the remained of the catalog in InDesign and want the cover created in InDesign. I will provide photos.

Looking to beable to add the cover to our existing attached catalog.

Industry/Entity Type

Manufacturing

Requirements
Must have
• Colors match what we are currently using. The Dark grey and gold
Nice to have
• modern, clean

```html
<!DOCTYPE html>
<html lang="en">
<head>
<meta charset="utf-8">
<title>Paramount Polymers – Catalog Cover</title>
<link href="https://fonts.googleapis.com/css2?family=Bebas+Neue&display=swap" rel="stylesheet">
<style>
  :root {
    --charcoal: #3b3b3b;
    --charcoal-deep: #2e2e2e;
    --gold: #d9bb78;
    --gold-deep: #c9a45c;
    --paper: #ffffff;
    --mist: #e4e4e4;
    --ink: #3a3a3a;
  }
  * { margin: 0; padding: 0; box-sizing: border-box; }
  html, body { width: 849px; height: 1200px; overflow: hidden; background: var(--paper); }
  .cover {
    position: relative;
    width: 849px;
    height: 1200px;
    background: var(--paper);
    overflow: hidden;
    font-family: "Bebas Neue", "Oswald", sans-serif;
  }
  .cover-shapes { position: absolute; inset: 0; }
  .brand {
    position: absolute;
    left: 538px;
    top: 56px;
    display: flex;
    align-items: center;
    gap: 16px;
  }
  .brand-dot {
    width: 74px;
    height: 74px;
    border-radius: 50%;
    background: var(--gold);
    flex: none;
  }
  .brand-name {
    color: var(--paper);
    font-size: 37px;
    line-height: 44px;
    letter-spacing: 0.5px;
  }
  .headline {
    position: absolute;
    left: 58px;
    top: 168px;
    color: var(--ink);
  }
  .headline-kicker {
    font-size: 35px;
    line-height: 40px;
    letter-spacing: 0.3px;
    font-weight: 400;
  }
  .headline-title {
    font-size: 130px;
    line-height: 112px;
    letter-spacing: 1px;
    font-weight: 400;
    margin-top: 0;
  }
  .headline-line { display: block; }
  .contact {
    position: absolute;
    left: 64px;
    top: 1082px;
    color: var(--paper);
    font-size: 19px;
    line-height: 21px;
    letter-spacing: 0.3px;
    font-style: normal;
  }
  .contact-row { display: flex; align-items: flex-start; gap: 8px; }
  .contact-row + .contact-row { margin-top: 6px; }
  .contact-icon { width: 16px; height: 16px; flex: none; margin-top: 12px; }
  .contact-row.web .contact-icon { margin-top: 2px; }
  .footer-band {
    position: absolute;
    left: 0;
    bottom: 0;
    width: 849px;
    height: 10px;
    background: var(--gold);
  }
</style>
</head>
<body>
<main class="cover">
  <svg class="cover-shapes" width="849" height="1200" viewBox="0 0 849 1200">
    <defs>
      <linearGradient id="lineFieldTone" x1="0" y1="0" x2="1" y2="1">
        <stop offset="0" stop-color="#ececec"/>
        <stop offset="1" stop-color="#f7f7f7"/>
      </linearGradient>
      <linearGradient id="productTone" x1="0" y1="0" x2="0" y2="1">
        <stop offset="0" stop-color="#555555"/>
        <stop offset="0.55" stop-color="#3d3d3d"/>
        <stop offset="0.7" stop-color="#b89a5c"/>
        <stop offset="1" stop-color="#ddc07e"/>
      </linearGradient>
    </defs>

    <path class="wave-top" d="M300 0 C360 110 420 200 560 270 C680 330 780 360 849 410 L849 0 Z" fill="var(--charcoal)"/>
    <path d="M300 0 C360 110 420 200 560 270 C680 330 780 360 849 410" fill="none" stroke="var(--gold-deep)" stroke-width="4"/>

    <path role="img" aria-label="Decorative field of fine grey flowing lines"
          d="M0 400 C250 420 560 440 849 470 L849 900 C700 830 600 760 560 700 L0 560 Z"
          fill="url(#lineFieldTone)"/>

    <path class="wave-bottom" d="M0 880 C250 900 470 890 540 912 C680 960 760 1010 849 1066 L849 1200 L0 1200 Z" fill="var(--charcoal)"/>
    <path d="M540 912 C680 960 760 1010 849 1066" fill="none" stroke="var(--gold-deep)" stroke-width="4"/>

    <circle cx="241" cy="754" r="308" fill="var(--paper)"/>
    <circle role="img" aria-label="Photo of coiled black, grey, orange and blue rubber extrusion seals and gaskets on a gold surface"
            cx="241" cy="754" r="298" fill="url(#productTone)"/>
  </svg>

  <div class="brand">
    <span class="brand-dot"></span>
    <div class="brand-name">Paramount<br>Polymers</div>
  </div>

  <header class="headline">
    <p class="headline-kicker">RUBBER &amp; PLASTIC EXTURSION</p>
    <h1 class="headline-title"><span class="headline-line">GASKETS,</span><span class="headline-line">TRIMS &amp; SEALS</span></h1>
  </header>

  <address class="contact">
    <div class="contact-row phone">
      <svg class="contact-icon" viewBox="0 0 16 16"><path d="M3 2 L6 2 L7 5 L5 6.5 C6 8.5 7.5 10 9.5 11 L11 9 L14 10 L14 13 C8 13.5 2.5 8 3 2 Z" fill="var(--gold)"/></svg>
      <div>888-555-0142<br>330-555-0187</div>
    </div>
    <div class="contact-row web">
      <svg class="contact-icon" viewBox="0 0 16 16"><circle cx="8" cy="8" r="6.5" fill="none" stroke="var(--gold)" stroke-width="1.5"/><ellipse cx="8" cy="8" rx="2.8" ry="6.5" fill="none" stroke="var(--gold)" stroke-width="1.2"/><path d="M1.5 8 H14.5 M2.5 5 H13.5 M2.5 11 H13.5" stroke="var(--gold)" stroke-width="1.1"/></svg>
      <div>WWW.PARAMOUNTPOLYMERS.COM</div>
    </div>
  </address>

  <div class="footer-band"></div>
</main>
</body>
</html>
```